Wedding Startup Full Website Design

We've just completed our online platform and need to create a website that represents our brand and vision, and clearly communicates our features and value proposition to potential users. There are a minimum of 4 pages that need to be designed. One geared toward wedding professionals (venues/vendors/coordinators), another toward engaged couples, one showcasing features, and an 'About Us' page.

The designer will creative freedom to create a unique UI/UX as long as it represents our brand and is relevant to our target audience/market. The ideal candidate will be able to assume the mindset of someone working in the wedding industry and/or an engaged couple. Ability to create illustrations is a plus.

Copy will be provided as needed. We will reimburse for stock images (pending approval before purchasing), but sourcing the stock images will be the responsibility of the designer.

Our current website: https://www.trelmora.com
Updates

Our project has now been guaranteed! We look forward to finding the perfect design for our site pages!

Still waiting for a design that stands out from the rest and aligns with the creative brief.

Target Market(s)

Wedding Professionals and Engaged Couples

Industry/Entity Type

Wedding

Number of Pages Required

4 page

Font styles to use
Sans Serif

Colors
ffffff
fbd4d5
f59195
33a6d7
cadf82
86cfc6

Requirements
Must have
• Common sense stuff like having a unified brand that accurately represents our platform, speaks to our target market, and clearly articulates our vision
Nice to have
• Illustrations
Should not have
• Overly cheesy or childish. We want to be professional but still embrace the wedding culture.

```html
<!DOCTYPE html>
<html lang="en">
<head>
<meta charset="utf-8">
<title>Trelmora — Wedding Planning Platform</title>
<link href="https://fonts.googleapis.com/css2?family=Roboto:wght@400;500;700&family=Great+Vibes&family=Roboto+Slab:wght@400&display=swap" rel="stylesheet">
<style>
:root{
  --coral:#e86d6f;
  --coral-soft:#f59195;
  --blush:#fbd4d5;
  --sky:#5aa8e2;
  --sky-deep:#4a9bd8;
  --ink:#2b2b2b;
  --text:#555;
  --panel:#f7f7f7;
  --tile:#ececec;
  --news:#f2f2f2;
  --footer:#1b1b1b;
  --white:#fff;
}
*{box-sizing:border-box;margin:0;padding:0}
html,body{width:1200px;height:3377px;overflow:hidden}
body{position:relative;background:var(--white);font-family:"Roboto",Arial,sans-serif;color:var(--text)}
.abs{position:absolute}
.site-header{left:0;top:0;width:1200px;height:72px;border-top:4px solid var(--coral);background:var(--white)}
.brand{left:171px;top:16px;display:flex;align-items:center;gap:8px;font:500 30px "Roboto",sans-serif;color:var(--sky)}
.brand-dot{width:12px;height:12px;border-radius:50%;background:var(--coral)}
.main-nav{right:170px;top:28px;display:flex;gap:30px;font:500 13px "Roboto",sans-serif;color:var(--ink);letter-spacing:.3px}
.hero{left:0;top:72px;width:1200px;height:531px;background:linear-gradient(135deg,#dfe3e2 0%,#b9b3ad 35%,#6b5d55 55%,#e8e2dc 80%,#f3efea 100%)}
.value{top:652px;width:320px;text-align:center}
.value svg{display:block;margin:0 auto}
.value h3{margin-top:14px;font:500 14px "Roboto",sans-serif;color:var(--coral);letter-spacing:.5px}
.value p{margin-top:8px;font-size:12px;line-height:17px;color:var(--ink)}
.about-photo{left:173px;top:855px;width:426px;height:356px;background:linear-gradient(160deg,#efe9e4,#d9cbc0 50%,#b9a79a)}
.about-panel{left:599px;top:855px;width:430px;height:356px;background:var(--panel);padding:40px 34px}
.script{font-family:"Great Vibes",cursive;color:var(--ink);font-weight:400}
.about-panel h2{font-size:44px;line-height:50px}
.about-panel p{margin-top:14px;font-size:11.5px;line-height:17px;color:var(--ink)}
.btn-outline{display:inline-block;margin-top:26px;border:2px solid var(--coral);padding:8px 14px;font:500 11px "Roboto",sans-serif;color:var(--ink)}
.steps{left:0;top:1279px;width:1200px;height:337px;background:linear-gradient(180deg,var(--sky) 0%,#6fb3e6 100%)}
.steps h2{position:absolute;top:46px;width:100%;text-align:center;font:700 25px "Roboto",sans-serif;color:var(--white)}
.step{top:110px;width:280px;text-align:center;color:var(--white)}
.step-num{width:66px;height:66px;margin:0 auto;border-radius:50%;border:4px solid var(--white);background:rgba(255,255,255,.15);box-shadow:0 0 0 3px rgba(255,255,255,.35);font:400 36px/58px "Roboto Slab",serif}
.step h3{margin-top:14px;font:500 14px "Roboto",sans-serif}
.step p{margin-top:8px;font-size:11px;line-height:16px;color:#eaf4fc}
.ornament{width:90px;height:52px;left:555px;border-radius:26px;background:linear-gradient(90deg,#e9a3a6,#8fb38a 50%,#e9a3a6)}
.section-title{width:1200px;left:0;text-align:center;font-size:52px;line-height:60px}
.tile{width:203px;height:167px}
.features{left:0;top:2224px;width:1200px;height:297px;background:var(--coral)}
.feature{top:44px;width:300px;text-align:center;color:var(--white)}
.feature h3{margin-top:20px;font:500 14px "Roboto",sans-serif}
.feature p{margin-top:8px;font-size:11px;line-height:15px}
.why{top:2755px;width:149px;height:162px;background:var(--tile)}
.why svg{display:block;margin:28px auto 0}
.why span{position:absolute;left:0;bottom:0;width:100%;height:42px;background:var(--sky);color:var(--white);font:500 11.5px/42px "Roboto",sans-serif;text-align:center}
.newsletter{left:0;top:2983px;width:1200px;height:198px;background:var(--news);text-align:center}
.newsletter h2{margin-top:30px;font:700 26px "Roboto",sans-serif;color:var(--ink)}
.newsletter .rule{width:48px;height:2px;background:var(--coral);margin:8px auto 0}
.newsletter p{margin-top:8px;font-size:11px;color:var(--ink)}
.field{top:119px;height:32px;background:var(--white);border:1px solid #ddd;font-size:11px;color:#999;text-align:left;padding:9px 12px}
.btn-subscribe{top:119px;left:889px;width:160px;height:32px;background:var(--sky);color:var(--white);font:500 12px/32px "Roboto",sans-serif}
.site-footer{left:0;top:3181px;width:1200px;height:151px;background:var(--footer);color:#ddd}
.foot-col{top:44px;font-size:12px;line-height:19px}
.foot-col h4{display:flex;align-items:center;gap:8px;font:700 12px "Roboto",sans-serif;color:var(--white);margin-bottom:15px}
.bottom-bar{left:0;top:3332px;width:1200px;height:45px;background:var(--coral);color:var(--white)}
.bottom-links{left:173px;top:15px;font-size:11.5px}
.bottom-links b{font-weight:400;margin:0 12px}
.socials{left:912px;top:11px;display:flex;gap:7px}
.socials i{width:22px;height:22px;border:1.5px solid var(--white);border-radius:50%}
</style>
</head>
<body>

<header class="site-header abs">
  <div class="brand abs"><span class="brand-dot"></span>Trelmora</div>
  <nav class="main-nav abs"><span>ABOUT US</span><span>FEATURES</span><span>FOR COUPLES</span></nav>
</header>

<div class="hero abs" role="img" aria-label="Photo of a bride and groom embracing in a snowy outdoor setting beside a wedding cake"></div>

<section>
  <div class="value abs" style="left:121px">
    <svg width="80" height="80" viewBox="0 0 80 80" fill="none" stroke="#222" stroke-width="3"><circle cx="40" cy="30" r="12"/><path d="M35 44h10M40 10v-6M22 16l-5-5M58 16l5-5M18 30h-6M62 30h6"/><path d="M12 62h20l14-8c4-2 8 2 5 5l-12 9H12z" fill="#222"/></svg>
    <h3>INSPIRE</h3>
    <p>Inspire innovation and bringing dream<br>weddings to life.</p>
  </div>
  <div class="value abs" style="left:436px">
    <svg width="80" height="80" viewBox="0 0 80 80" fill="none" stroke="#222" stroke-width="3"><path d="M18 20h18l-3 20a6 6 0 0 1-12 0zM27 46v20M20 66h14M44 20h18l-3 20a6 6 0 0 1-12 0zM53 46v20M46 66h14M28 10l2-6M52 10l-2-6"/></svg>
    <h3>ENJOY</h3>
    <p>For wedding professions and couples to<br>enjoy the wedding planning experience.</p>
  </div>
  <div class="value abs" style="left:758px">
    <svg width="80" height="80" viewBox="0 0 80 80" fill="none" stroke="#222" stroke-width="3"><path d="M40 74V20M40 34c-8 0-14-6-14-14 8 0 14 6 14 14zM40 34c8 0 14-6 14-14-8 0-14 6-14 14zM40 52c-9 0-15-6-15-14 9 0 15 6 15 14zM40 52c9 0 15-6 15-14-9 0-15 6-15 14z"/></svg>
    <h3>GROW</h3>
    <p>Foster growth for our partners and within<br>the wedding industry.</p>
  </div>
</section>

<div class="about-photo abs" role="img" aria-label="Photo of a bride holding a bouquet of white and blush roses"></div>
<section class="about-panel abs">
  <h2 class="script">About Us</h2>
  <p>Weddings are one the most memorable events in people's life. Unfortunately planning a wedding is filled with stress, often leaving wedding professionals and their clients with soured memories.</p>
  <p>Our vision at Trelmora is to revamp the way weddings are planned on both sides of the process (wedding professionals and their clients). We aim to reduce the stress of everyone involved, and make the engagement season and wedding day memorable for the right reasons.</p>
  <span class="btn-outline">READ MORE &#10148;</span>
</section>

<section class="steps abs">
  <h2>HOW TO GET STARTED</h2>
  <div class="step abs" style="left:136px"><div class="step-num">1</div><h3>SIGN UP</h3><p>Create a free account on Trelmora to access<br>popular collaboration tools. Get Started</p></div>
  <div class="step abs" style="left:457px"><div class="step-num">2</div><h3>COLLABORATE</h3><p>Add clients within the application to better<br>organize and manage event details.</p></div>
  <div class="step abs" style="left:784px"><div class="step-num">3</div><h3>CONNECT</h3><p>Linking your bank account within Trelmora to<br>allow for seamless payments and monitoring.</p></div>
</section>

<div class="ornament abs" style="top:1668px" role="img" aria-label="Small floral ornament of pink roses and leaves"></div>
<h2 class="section-title script abs" style="top:1728px">Our Showcase</h2>

<div class="tile abs" style="left:173px;top:1817px;background:linear-gradient(180deg,#9cc7dc,#e7ddd0)" role="img" aria-label="Beach wedding arch with white chairs"></div>
<div class="tile abs" style="left:390px;top:1817px;background:linear-gradient(160deg,#6c7a55,#e8e4dc)" role="img" aria-label="Table centerpiece of white flowers"></div>
<div class="tile abs" style="left:607px;top:1817px;background:linear-gradient(180deg,#c7b7c3,#8a6f8f)" role="img" aria-label="Purple floral table setting"></div>
<div class="tile abs" style="left:824px;top:1817px;background:linear-gradient(160deg,#dcd8cf,#f2efe9)" role="img" aria-label="Glassware and white flowers on a banquet table"></div>
<div class="tile abs" style="left:173px;top:1994px;background:linear-gradient(180deg,#4f5d3e,#efe6da)" role="img" aria-label="White sofa framed by garden flowers"></div>
<div class="tile abs" style="left:390px;top:1994px;background:linear-gradient(160deg,#d9c6d8,#b59bb8)" role="img" aria-label="Lavender and white roses"></div>
<div class="tile abs" style="left:607px;top:1994px;background:linear-gradient(180deg,#e7e3da,#8da06c)" role="img" aria-label="Birdcage centerpiece with flowers"></div>
<div class="tile abs" style="left:824px;top:1994px;background:linear-gradient(160deg,#cdc6bb,#f1ede6)" role="img" aria-label="Candles and white flowers on a reception table"></div>

<section class="features abs">
  <div class="feature abs" style="left:150px">
    <svg width="60" height="70" viewBox="0 0 60 70" fill="none" stroke="#fff" stroke-width="3"><path d="M12 4h36M12 66h36M16 4c0 18 28 22 28 31S16 48 16 66M44 4c0 18-28 22-28 31s28 13 28 31"/></svg>
    <h3>Realtime Collaboration</h3>
    <p>There are often disconnects in the communication channel. At the core of Trelmora we ensure everyone is updated in real time with event information.</p>
  </div>
  <div class="feature abs" style="left:440px">
    <svg width="80" height="70" viewBox="0 0 80 70" fill="none" stroke="#fff" stroke-width="3"><path d="M22 50h-4a14 14 0 0 1 0-28 20 20 0 0 1 38-4 14 14 0 0 1 6 32h-4M40 66V32M30 42l10-10 10 10"/></svg>
    <h3>Cloud Storage</h3>
    <p>No longer do you have to remember where every piece of information is saved. With Trelmora all your information is available in one central location.</p>
  </div>
  <div class="feature abs" style="left:746px">
    <svg width="70" height="70" viewBox="0 0 70 70" fill="none" stroke="#fff" stroke-width="3"><path d="M17 50V32a18 18 0 0 1 36 0v18l5 6H12zM29 62a6 6 0 0 0 12 0M8 24a28 28 0 0 1 8-12M62 24a28 28 0 0 0-8-12"/></svg>
    <h3>Notifications &amp; Deadlines</h3>
    <p>No longer do you have to remember where every piece of information is saved. With Trelmora all your information is available in one central location.</p>
  </div>
</section>

<div class="ornament abs" style="top:2591px" role="img" aria-label="Small floral ornament of pink roses and leaves"></div>
<h2 class="section-title script abs" style="top:2656px">Why Trelmora</h2>

<div class="why abs" style="left:173px"><svg width="76" height="76" viewBox="0 0 76 76" fill="none" stroke="#333" stroke-width="3"><path d="M14 38a24 24 0 1 0 8-18M22 8v12H10"/><text x="38" y="45" text-anchor="middle" font-family="Roboto,sans-serif" font-size="20" font-weight="700" fill="#333" stroke="none">24</text></svg><span>Saves Everyone Time</span></div>
<div class="why abs" style="left:351px"><svg width="70" height="70" viewBox="0 0 70 70" fill="none" stroke="#333" stroke-width="3"><rect x="10" y="14" width="50" height="46"/><path d="M10 26h50M22 8v10M48 8v10M18 34h8M31 34h8M44 34h8M18 44h8M31 44h8M44 44h8"/></svg><span>Simplified Organization</span></div>
<div class="why abs" style="left:527px"><svg width="70" height="70" viewBox="0 0 70 70" fill="none" stroke="#333" stroke-width="3"><path d="M14 30h10v24H14zM24 32l10-18c4 0 6 3 5 7l-2 7h14c3 0 5 3 4 6l-4 14c-1 3-3 4-6 4H24M14 64l3 2M28 62l4-4 4 4M42 62l4-4 4 4"/></svg><span>Simplified Organization</span></div>
<div class="why abs" style="left:703px"><svg width="76" height="70" viewBox="0 0 76 70" fill="none" stroke="#333" stroke-width="3"><rect x="8" y="22" width="46" height="30" rx="3"/><path d="M8 30h46M20 14l42-4 4 30-12 2M50 40h12"/></svg><span>Lower Transaction Fees</span></div>
<div class="why abs" style="left:879px"><svg width="76" height="70" viewBox="0 0 76 70" fill="none" stroke="#333" stroke-width="3"><rect x="10" y="14" width="46" height="32"/><path d="M26 54h16M34 46v8"/><rect x="50" y="28" width="16" height="28"/></svg><span>Accessible on Any Device</span></div>

<section class="newsletter abs">
  <h2>SUBSCRIBE TO OUR NEWSLETTER</h2>
  <div class="rule"></div>
  <p>If you want to receive monthly updates from us just pop your email in the box.</p>
  <div class="field abs" style="left:173px;width:352px">Enter your name</div>
  <div class="field abs" style="left:536px;width:340px">Enter your email address</div>
  <div class="btn-subscribe abs">SUBSCRIBE NOW</div>
</section>

<footer class="site-footer abs">
  <div class="foot-col abs" style="left:173px">
    <h4><svg width="12" height="16" viewBox="0 0 12 16"><path d="M6 0a6 6 0 0 1 6 6c0 4-6 10-6 10S0 10 0 6a6 6 0 0 1 6-6z" fill="#fff"/><circle cx="6" cy="6" r="2" fill="#1b1b1b"/></svg>OUR ADDRESS</h4>
    418 Linden Grove Ave<br>Maplewood, GA, United States
  </div>
  <div class="foot-col abs" style="left:536px">
    <h4><svg width="16" height="12" viewBox="0 0 16 12"><rect width="16" height="12" fill="#fff"/><path d="M0 0l8 7 8-7" fill="none" stroke="#1b1b1b" stroke-width="1.5"/></svg>CONTACT US</h4>
    +1 800 555 0142<br>info@trelmora.com
  </div>
  <div class="foot-col abs" style="left:891px">
    <h4><svg width="14" height="14" viewBox="0 0 14 14"><circle cx="7" cy="7" r="6" fill="none" stroke="#fff" stroke-width="2"/><path d="M7 3v4l3 2" stroke="#fff" stroke-width="1.6" fill="none"/></svg>OFFICE HOURS</h4>
    Monday to Friday: 8:00 - 17:00<br>Saturday, Sunday: 9:00 - 14:00
  </div>
</footer>

<div class="bottom-bar abs">
  <div class="bottom-links abs">About Us<b>|</b>Features<b>|</b>For Couples</div>
  <div class="socials abs"><i></i><i></i><i></i><i></i><i></i></div>
</div>

</body>
</html>
```